Website design for legal tech start up in Switzerland (B2B)

We are for a legal tech start up in Switzerland called TAVO. We have been running since August 2016. This will be our first live website.

We need a website designed and business card design for our start-up in Switzerland. We also need the Web design to be converted into HTML and CSS files.

Function of website:
• To inform potential customers of our services
• Form a key part of our digital marketing and sales footprint.
• Branding

Please find attached logo.
Updates

Project Deadline Extended Reason: Giving us time to review submissions and provide opportunity for more submissions. Added Thursday, February 16, 2017

Reason: Looking for more idea's not necessarily set on blue and grey colours only.

Target Market(s)

B2B tech powered legal services.

Industry/Entity Type

Legal

Contact Information for Business Card

Lean and slick design.

Coding

Coded - Design and coding required

Number of Pages Required

5+ page

Requirements
Must have
• VERY LEAN AND CLEAN DESIGN!
• We have received many great standard designs, but we are looking for something more out-of-the box: You can get inspiration from these designs: http://www.pindelsite.com/websites/clean/
• Thanks!!
• Easy content management system
• Well structured coding for additional development
• Responsive webpage for all types of devices
• SEO optimized
• Tabs (Home, services, team, careers, blog, contact us)
• Colour scheme complementary to logo
Nice to have
• Look and Design - Approachable, High-tech, Modern
• Easy to add chat bot capability in future
Should not have
• Too busy/ too much clutter
• Not take to long to load

```html
<!DOCTYPE html>
<html lang="en">
<head>
<meta charset="utf-8">
<title>TAVO – Legal Services</title>
<link href="https://fonts.googleapis.com/css2?family=Roboto:ital,wght@0,300;0,400;0,500;0,700;1,400&display=swap" rel="stylesheet">
<style>
:root{
  --blue-dark:#2c4a8e;
  --blue:#3d5fa8;
  --blue-light:#5f81c6;
  --title:#2e4a8f;
  --ink:#222;
  --muted:#666;
  --soft:#f4f5f7;
  --line:#e2e4e8;
  --white:#fff;
}
*{box-sizing:border-box;margin:0;padding:0}
html,body{width:1200px;height:2503px;overflow:hidden}
body{font-family:'Roboto',sans-serif;color:var(--ink);background:var(--white);position:relative}
.wrap{width:1098px;margin:0 auto;position:relative}
.section-title{font-size:22px;font-weight:500;text-align:center;color:var(--ink)}
.section-title span{color:var(--title)}
.dots{border-bottom:2px dotted var(--blue-light);margin-top:14px}

/* hero */
.hero{height:545px;position:relative;color:var(--white);
  background:linear-gradient(120deg,#4a4e56 0%,#7c7f86 35%,#5b5e64 60%,#9a9ca1 100%)}
.hero-photo{position:absolute;inset:0}
.hero-shade{position:absolute;inset:0;background:rgba(20,24,32,.35)}
.site-header{position:absolute;top:0;left:0;right:0;height:67px;border-bottom:1px solid rgba(255,255,255,.25)}
.site-header .wrap{display:flex;align-items:center;height:67px}
.brand{font-size:38px;font-weight:700;letter-spacing:2px;color:var(--white);width:240px}
.nav{display:flex;gap:38px;font-size:15px;font-weight:500;margin-left:50px}
.nav a{color:var(--white);text-decoration:none}
.header-actions{margin-left:auto;display:flex;gap:10px}
.pill{border:2px solid var(--white);border-radius:18px;padding:6px 14px;font-size:13px;font-weight:500;color:var(--white)}
.pill.solid{background:var(--white);color:var(--ink)}
.hero-copy{position:absolute;top:230px;left:0;right:0;text-align:center}
.hero-copy h1{font-size:20px;font-weight:700}
.hero-copy p{width:420px;margin:14px auto 0;font-size:11px;line-height:22px}
.btn-ghost{display:inline-block;margin-top:18px;border:2px solid var(--white);border-radius:4px;padding:8px 16px;font-size:12px;font-weight:500;color:var(--white)}

/* welcome */
.welcome{height:110px;background:linear-gradient(90deg,var(--blue-dark),var(--blue-light));color:var(--white);text-align:center;padding-top:4px}
.welcome h2{font-size:21px;font-weight:500}
.welcome .dots{border-color:rgba(255,255,255,.8);margin-top:12px}
.welcome p{font-size:12px;line-height:20px;margin-top:14px;padding:0 40px}

/* services */
.services{height:310px;background:var(--soft);padding-top:18px}
.service-grid{display:flex;gap:27px;margin-top:46px}
.service{width:254px;height:145px;position:relative;border-radius:4px}
.service-img{position:absolute;inset:0;border-radius:4px}
.service-icon{position:absolute;top:-23px;left:104px;width:46px;height:46px;border-radius:50%;background:var(--blue);border:3px solid var(--white);display:flex;align-items:center;justify-content:center}
.service-label{position:absolute;left:12px;right:12px;bottom:-12px;height:40px;background:var(--blue);border-radius:4px;color:var(--white);font-size:16px;font-weight:500;display:flex;align-items:center;justify-content:center}

/* mail bar */
.mailbar{height:88px;background:linear-gradient(90deg,var(--blue-dark),var(--blue-light));color:var(--white)}
.mailbar .wrap{display:flex;align-items:center;height:88px;gap:18px}
.mailbar .label{font-size:13px;font-weight:500;width:110px;margin-left:10px}
.field{width:253px;height:34px;background:var(--white);border-radius:3px;color:#999;font-size:13px;padding:9px 12px}
.submit{width:94px;height:34px;background:var(--white);border-radius:3px;color:var(--ink);font-weight:700;font-size:13px;text-align:center;padding-top:9px}

/* blog */
.blog{height:455px;padding-top:6px}
.post-grid{display:flex;gap:27px;margin-top:32px}
.post{width:254px;height:356px;background:var(--soft)}
.post-img{height:189px}
.post-body{padding:14px 19px}
.post h3{font-size:18px;font-weight:500}
.post p{font-size:12.5px;line-height:20px;color:var(--muted);margin-top:8px;height:62px}
.post-meta{border-top:1px solid var(--line);margin-top:12px;padding-top:12px;display:flex;justify-content:space-between;font-size:11px;color:var(--muted)}
.post-meta span{display:flex;align-items:center;gap:5px}

/* in-house */
.inhouse{height:285px;position:relative;color:var(--white);text-align:center;
  background:linear-gradient(100deg,#5d7ab4 0%,#8aa0c8 40%,#6f86b5 70%,#3e5a96 100%)}
.inhouse h2{padding-top:62px;font-size:32px;font-weight:400}
.inhouse .rule{width:26px;border-top:2px solid var(--white);margin:14px auto 0}
.inhouse p{font-size:18px;line-height:27px;margin-top:22px;font-weight:300}
.inhouse .btn-ghost{margin-top:16px;font-size:13px;padding:8px 24px}

/* testimonials */
.testimonials{height:217px;background:var(--soft);padding-top:24px}
.quotes{display:flex;margin-top:28px}
.quote{width:549px;display:flex;align-items:flex-start;gap:18px}
.quote.left{padding-right:20px;text-align:right}
.quote.right{padding-left:20px;border-left:2px dotted #aaa}
.quote p{font-size:12.5px;font-style:italic;line-height:20px;color:var(--muted)}
.quote .who{font-size:13px;font-weight:500;color:var(--ink);margin-top:12px;font-style:normal}
.avatar{width:76px;height:76px;border-radius:50%;flex:none;background:#c9b8a7;border:3px solid var(--white)}

/* like strip */
.likestrip{height:75px;position:relative}
.likestrip .track{position:absolute;top:36px;left:65px;right:65px;border-top:1px solid var(--line)}
.likebox{position:absolute;left:378px;top:15px;width:448px;height:46px;border:1px solid var(--line);border-radius:23px;background:var(--white);display:flex;align-items:center;gap:14px;padding-left:58px;font-size:10px;color:#444}
.likebox .thumb{position:absolute;left:0;top:0;width:46px;height:44px;border-right:1px solid var(--line);display:flex;align-items:center;justify-content:center}
.likebtn{background:var(--blue);color:var(--white);font-weight:700;padding:3px 7px;border-radius:2px;font-size:10px}

/* footer */
.site-footer{height:418px;background:linear-gradient(110deg,var(--blue-dark),var(--blue-light));color:var(--white)}
.footer-cols{display:flex;padding-top:26px;height:348px}
.footer-cols h4{font-size:17px;font-weight:500}
.col-contact{width:282px}
.col-map{width:534px;text-align:center}
.col-about{width:282px;padding-left:28px}
.site-footer p{font-size:12.5px;line-height:20px;margin-top:18px}
.site-footer b{font-weight:700}
.map{width:534px;height:223px;margin-top:15px;background:linear-gradient(135deg,#cfe0ee,#e9e4d8 45%,#d6e4c9 70%,#bcd3e6)}
.socials{display:flex;gap:12px;margin-top:22px}
.socials i{width:13px;height:13px;border-radius:50%;background:var(--white);display:block}
.footer-bottom{border-top:1px solid rgba(255,255,255,.5);display:flex;justify-content:space-between;align-items:center;padding-top:14px;font-size:11px;font-weight:500}
.footer-bottom .brand{font-size:34px;width:auto}
</style>
</head>
<body>

<header class="hero">
  <div class="hero-photo" role="img" aria-label="Photo of businessmen in suits talking in a meeting"></div>
  <div class="hero-shade"></div>
  <div class="site-header">
    <div class="wrap">
      <div class="brand">TAVO</div>
      <nav class="nav"><a>HOME</a><a>SERVICES</a><a>TEAM</a><a>CAREERS</a><a>BLOG</a><a>CONTACT</a></nav>
      <div class="header-actions"><span class="pill">Chat</span><span class="pill solid">Free Evaluation</span></div>
    </div>
  </div>
  <div class="hero-copy">
    <h1>We Provide Legal Help for Felonies</h1>
    <p>At vero eos et accusamus et iusto odio dignissimos ducimus qui blanditiis praesentium voluptatum deleniti atque corrupti quos dolores et quas molestias excepturi sint occaecati cupiditate non provident.</p>
    <span class="btn-ghost">LEARN MORE</span>
  </div>
</header>

<section class="welcome">
  <div class="wrap">
    <h2>Welcome to TAVO</h2>
    <div class="dots"></div>
    <p>Sed ut perspiciatis unde omnis iste natus error sit voluptatem accusantium doloremque laudantium, totam rem aperiam, eaque ipsa quae ab illo inventore veritatis et quasi architecto beatae vitae dicta sunt explicabo</p>
  </div>
</section>

<section class="services">
  <div class="wrap">
    <h2 class="section-title">Our <span>Services</span></h2>
    <div class="dots"></div>
    <div class="service-grid">
      <div class="service">
        <div class="service-img" role="img" aria-label="Photo of hands in handcuffs" style="background:linear-gradient(135deg,#8a6a5c,#c9a594 50%,#6b5047)"></div>
        <div class="service-icon"><svg width="20" height="20" viewBox="0 0 20 20"><rect x="3" y="3" width="9" height="5" rx="1" fill="#fff" transform="rotate(-35 7 5)"/><rect x="8" y="8" width="2.5" height="10" fill="#fff" transform="rotate(-35 9 13)"/><rect x="2" y="16" width="9" height="2" fill="#fff"/></svg></div>
        <div class="service-label">Criminal Charges</div>
      </div>
      <div class="service">
        <div class="service-img" role="img" aria-label="Photo of a small wooden house model on documents" style="background:linear-gradient(135deg,#e9dcc4,#c8a97c 50%,#f1ebe1)"></div>
        <div class="service-icon"><svg width="20" height="20" viewBox="0 0 20 20"><path d="M2 10 L10 3 L18 10 L16 10 L16 17 L4 17 L4 10 Z" fill="#fff"/><rect x="8" y="11" width="4" height="6" fill="#3d5fa8"/></svg></div>
        <div class="service-label">Estate Planning</div>
      </div>
      <div class="service">
        <div class="service-img" role="img" aria-label="Photo of city office towers against the sky" style="background:linear-gradient(180deg,#7fa7d6,#b6c9dd 50%,#5c6f86)"></div>
        <div class="service-icon"><svg width="20" height="20" viewBox="0 0 20 20"><rect x="3" y="11" width="3" height="6" fill="#fff"/><rect x="8.5" y="8" width="3" height="9" fill="#fff"/><rect x="14" y="5" width="3" height="12" fill="#fff"/></svg></div>
        <div class="service-label">Capital Market</div>
      </div>
      <div class="service">
        <div class="service-img" role="img" aria-label="Photo of a distressed driver beside a damaged car" style="background:linear-gradient(135deg,#6a4b43,#2f3a58 55%,#4a5f8e)"></div>
        <div class="service-icon"><svg width="22" height="20" viewBox="0 0 22 20"><path d="M3 12 L5 6 L17 6 L19 12 L19 16 L3 16 Z" fill="#fff"/><circle cx="7" cy="14" r="1.6" fill="#3d5fa8"/><circle cx="15" cy="14" r="1.6" fill="#3d5fa8"/></svg></div>
        <div class="service-label">Personal Injury</div>
      </div>
    </div>
  </div>
</section>

<section class="mailbar">
  <div class="wrap">
    <svg width="34" height="30" viewBox="0 0 34 30"><path d="M2 14 L32 2 L24 28 L15 18 Z M15 18 L32 2" fill="none" stroke="#fff" stroke-width="2" stroke-linejoin="round"/></svg>
    <div class="label">Feel Free to Mail</div>
    <div class="field">Full Name *</div>
    <div class="field">Phone Number *</div>
    <div class="field">Your Email *</div>
    <div class="submit">SUBMIT</div>
  </div>
</section>

<section class="blog">
  <div class="wrap">
    <h2 class="section-title">Latest <span>Blog &amp; Posts</span></h2>
    <div class="dots"></div>
    <div class="post-grid">
      <article class="post">
        <div class="post-img" role="img" aria-label="Photo of a traveller with a leather bag walking through a doorway" style="background:linear-gradient(90deg,#3b3530,#8b6a4f 60%,#5a3b23)"></div>
        <div class="post-body"><h3>Standard Post</h3><p>Enim congue blandit. Lorem ipsum dolor sit amet, consectetur adipiscing elit. Quisque...</p>
        <div class="post-meta"><span>▦ 22 June, 2015</span><span>● 0</span></div></div>
      </article>
      <article class="post">
        <div class="post-img" role="img" aria-label="Photo of a glass coffee carafe on a table" style="background:linear-gradient(135deg,#e8e6e1,#c9c3b6 50%,#6f7a5c)"></div>
        <div class="post-body"><h3>Video Post</h3><p>Ultrices posuere cubilia curae curabitur sit amet tortor ut massa commodo. Vestibulum...</p>
        <div class="post-meta"><span>▦ 22 June, 2015</span><span>● 0</span></div></div>
      </article>
      <article class="post">
        <div class="post-img" role="img" aria-label="Photo of a white chair by a brick wall" style="background:linear-gradient(135deg,#6e4a3a,#a8765a 50%,#c9a27a)"></div>
        <div class="post-body"><h3>Post with Image</h3><p>Enim congue blandit. Lorem ipsum dolor sit amet, consectetur adipiscing elit. Quisque...</p>
        <div class="post-meta"><span>▦ 22 June, 2015</span><span>● 0</span></div></div>
      </article>
      <article class="post">
        <div class="post-img" role="img" aria-label="Photo of an old leather notebook on a desk" style="background:linear-gradient(135deg,#d8cfc2,#9a7a5e 50%,#e4ddd2)"></div>
        <div class="post-body"><h3>Image Post</h3><p>Ultrices posuere cubilia curae curabitur sit amet tortor ut massa commodo. Vestibulum...</p>
        <div class="post-meta"><span>▦ 22 June, 2015</span><span>● 3</span></div></div>
      </article>
    </div>
  </div>
</section>

<section class="inhouse" role="img" aria-label="Blurred photo of a business meeting at a desk">
  <h2>In-house Legal Services</h2>
  <div class="rule"></div>
  <p>We have a range of services to help in-house lawyers.<br>Take a look and see how we can help you and your team.</p>
  <span class="btn-ghost">Learn More</span>
</section>

<section class="testimonials">
  <div class="wrap">
    <h2 class="section-title">What <span>People Say</span></h2>
    <div class="dots"></div>
    <div class="quotes">
      <div class="quote left">
        <div><p>Duis aute irure dolor in reprehenderit in voluptate velit esse cillum dolore eu fugiat nulla pariatur. Excepteur sint occaecat cupidatat non proident, sunt in culpa qui officia deserunt mollit.</p>
        <p class="who">Marc Aubert, Operations Manager</p></div>
        <div class="avatar" role="img" aria-label="Portrait photo of Marc Aubert"></div>
      </div>
      <div class="quote right">
        <div class="avatar" role="img" aria-label="Portrait photo of Nina Keller" style="background:#b89a82"></div>
        <div><p>Provident, similique sunt in culpa qui officia deserunt mollitia animi, id est laborum et dolorum fuga. Et harum quidem rerum facilis est et expedita distinctio. Nam libero tempore, cum soluta nobis.</p>
        <p class="who">Nina Keller, Creative Designer</p></div>
      </div>
    </div>
  </div>
</section>

<section class="likestrip">
  <div class="track"></div>
  <div class="likebox">
    <div class="thumb"><svg width="18" height="18" viewBox="0 0 18 18"><rect x="2" y="8" width="3" height="8" fill="#ccc"/><path d="M6 8 L9 2 L11 3 L10 7 L15 7 L14 16 L6 16 Z" fill="#ccc"/></svg></div>
    <span class="likebtn">✓ Like</span>
    <span>You and 4k others like this.</span>
  </div>
</section>

<footer class="site-footer">
  <div class="wrap">
    <div class="footer-cols">
      <div class="col-contact">
        <h4>Contact Us</h4>
        <p>Please feel free to contact us for any issue. Our staff is available to you from 9AM until 5PM on weekdays.</p>
        <p><b>Phone:</b> +41 44 310 22 18</p>
        <p><b>Office:</b> Company Address Here</p>
        <p><b>Email:</b> info@tavo-legal.ch</p>
        <div class="socials"><i></i><i></i><i></i><i></i><i></i></div>
      </div>
      <div class="col-map">
        <h4>Headquarters</h4>
        <div class="map" role="img" aria-label="Street map showing the headquarters location"></div>
      </div>
      <div class="col-about">
        <h4>About Team</h4>
        <p>Enim congue blandit. Lorem ipsum dolor sit amet, consectetur adipiscing elit. Quisque consectetur interdum finibus. Vestibulum ante ipsum primis in faucibus orci. luctus et ultrices posuere.</p>
        <p>Cubilia cras blandit finibus ipsum, id porttitor arcu volutpat a. Integer iaculis erat nec justo malesuada faucibus vel tempus sapien. Vivamus aliquam euismod tristique.</p>
      </div>
    </div>
    <div class="footer-bottom">
      <span>Copyright © TAVO</span>
      <span class="brand">TAVO</span>
      <span>All rights reserved</span>
    </div>
  </div>
</footer>

</body>
</html>
```